bright-vale.net Real Estate, Investment, Financial corporate

Real Estate, Investment, Financial corporate looking site. Show present a professional firm, with an elegant display. Please see the attached file which includes the logo, palette and fonts.
Updates

We just starting the brief today. ( logo was delayed)

Target Market(s)

Investors, Corporate , B2b

Industry/Entity Type

real-estate investments

Number of Pages Required

3 page

Requirements
Must have
• Dazzling Homepage
Nice to have
• paralex

```html
<!DOCTYPE html>
<html lang="en">
<head>
<meta charset="utf-8">
<title>Bright Vale — Real Estate</title>
<link href="https://fonts.googleapis.com/css2?family=Poppins:ital,wght@0,400;0,500;0,600;0,700;0,800;1,400&display=swap" rel="stylesheet">
<style>
:root{
  --accent:#f5cd97;
  --dark:#2b2b2b;
  --ink:#1e1e1e;
  --muted:#6b6b6b;
  --light:#f6f6f8;
  --grey:#dcdcdc;
  --white:#ffffff;
}
*{margin:0;padding:0;box-sizing:border-box}
html,body{width:1200px;height:4591px;overflow:hidden;background:var(--white)}
body{font-family:'Poppins',sans-serif;color:var(--ink)}
.page{position:relative;width:1200px;height:4591px}

/* header / hero */
.hero-art{position:absolute;left:0;top:0}
.brand{position:absolute;left:89px;top:40px;font-size:24px;font-weight:500;color:var(--accent);letter-spacing:.3px}
.nav{position:absolute;right:89px;top:42px;display:flex;gap:36px;list-style:none}
.nav li{font-size:13px;font-weight:500;color:var(--white)}
.welcome{position:absolute;left:180px;top:243px;font-size:22px;font-weight:500;color:var(--white);letter-spacing:.5px}
.hero-title{position:absolute;left:172px;top:262px;font-size:156px;font-weight:700;color:var(--white);letter-spacing:-1px;line-height:1;white-space:nowrap}
.btn-quote{position:absolute;left:505px;top:430px;width:190px;height:44px;background:var(--accent);color:var(--dark);font-size:14px;font-weight:600;display:flex;align-items:center;justify-content:center;letter-spacing:.5px}
.scroll-btn{position:absolute;left:1013px;top:565px;width:96px;height:96px;border-radius:50%;background:var(--white);box-shadow:0 8px 24px rgba(0,0,0,.15);display:flex;align-items:center;justify-content:center}
.slide-rail{position:absolute;left:1155px;top:285px;width:2px;height:125px;background:rgba(255,255,255,.3)}
.slide-rail span{position:absolute;left:-1px;top:45px;width:4px;height:35px;background:var(--white)}

/* headings */
.section-title{position:absolute;left:0;width:1200px;text-align:center;font-size:46px;font-weight:700;line-height:1}
.section-title::after{content:"";display:block;width:40px;height:3px;background:var(--accent);margin:16px auto 0}
.section-title.on-dark{color:var(--white)}

/* about */
.about-mark{position:absolute;left:566px;top:817px;width:68px;height:66px;border:3px solid var(--accent)}
.about-text{position:absolute;left:0;top:982px;width:1200px;text-align:center;font-size:18px;line-height:27px;color:#444;white-space:nowrap}
.text-link{position:absolute;font-size:12px;font-weight:600;text-decoration:underline;letter-spacing:.4px;color:var(--ink)}

/* feature card */
.feature{position:absolute;left:173px;top:1284px;width:658px;height:643px;background:var(--accent)}
.feature h3{position:absolute;left:57px;top:38px;font-size:28px;font-weight:700}
.feature p{position:absolute;left:57px;top:82px;width:520px;font-size:13.5px;line-height:20px;color:#3a3a3a}
.photo{position:absolute}
.eye-btn{position:absolute;left:774px;top:1687px;width:92px;height:92px;border-radius:50%;background:var(--white);display:flex;align-items:center;justify-content:center;box-shadow:0 6px 20px rgba(0,0,0,.15)}
.pager{position:absolute;left:850px;top:1860px;font-size:14px;color:#777;display:flex;gap:14px;align-items:center}
.pager b{color:var(--ink)}

/* portfolio */
.portfolio-bg{position:absolute;left:0;top:2079px}

/* testimonials */
.testimonial{position:absolute;width:470px;height:160px}
.avatar{position:absolute;left:0;top:0;width:128px;height:128px;border-radius:50%;border:5px solid var(--white);box-shadow:0 8px 24px rgba(0,0,0,.18);background:linear-gradient(160deg,#7a6a5c,#3a3431)}
.quote-mark{position:absolute;left:300px;top:-70px;font-size:180px;font-weight:800;font-style:italic;color:#ececec;line-height:1}
.testimonial blockquote{position:absolute;left:142px;top:6px;width:345px;font-size:18px;font-style:italic;line-height:22px;color:#444}
.testimonial .who{position:absolute;left:142px;top:117px;font-size:14px;font-weight:700;letter-spacing:.5px}
.testimonial .role{position:absolute;left:142px;top:139px;font-size:13px;color:var(--muted)}
.divider{position:absolute;left:89px;width:1022px;height:1px;background:#e2e2e2}

/* news */
.news-card{position:absolute;top:3384px;width:494px;height:453px;background:var(--white);box-shadow:0 12px 40px rgba(0,0,0,.1)}
.news-card .photo{left:9px;top:0;width:476px;height:294px}
.tag{position:absolute;left:33px;top:254px;background:var(--white);font-size:11px;font-weight:700;padding:3px 8px}
.news-card h4{position:absolute;left:30px;top:318px;font-size:20px;font-weight:600}
.news-card .date{position:absolute;left:30px;top:352px;font-size:12px;color:#555;display:flex;gap:8px;align-items:center}
.news-card p{position:absolute;left:30px;top:380px;width:440px;font-size:13px;line-height:22px;color:#555}

/* newsletter */
.newsletter{position:absolute;left:0;top:3958px;width:1200px;height:232px;background:var(--accent)}
.newsletter .kicker{position:absolute;left:89px;top:58px;font-size:22px;font-weight:600}
.newsletter h5{position:absolute;left:89px;top:80px;font-size:44px;font-weight:700;line-height:1.1}
.newsletter .note{position:absolute;left:89px;top:156px;font-size:13px;color:#555}
.signup{position:absolute;left:604px;top:91px;width:507px;height:50px;background:var(--white);display:flex;align-items:center}
.signup .field{flex:1;padding-left:28px;font-size:12px;color:#666;display:flex;gap:10px;align-items:center}
.signup .go{width:112px;height:42px;margin-right:4px;background:#151515;color:var(--white);font-size:13px;font-weight:600;display:flex;align-items:center;justify-content:center}

/* footer */
.footer{position:absolute;left:0;top:4190px;width:1200px;height:401px;background:var(--light)}
.footer .brand-big{position:absolute;left:89px;top:112px;width:312px;text-align:center;font-size:44px;font-weight:400;color:var(--accent)}
.footer .brand-sub{position:absolute;left:89px;top:173px;width:312px;text-align:center;font-size:14px;letter-spacing:5px;color:#444}
.col{position:absolute;top:72px}
.col h6{font-size:18px;font-weight:600;margin-bottom:14px}
.col li{list-style:none;font-size:13px;color:#555;line-height:27px}
.contact li{display:flex;gap:10px;line-height:18px;margin-bottom:12px;font-size:12.5px}
.footer .rule{position:absolute;left:89px;top:332px;width:1022px;height:1px;background:#dedede}
.copy{position:absolute;left:0;top:358px;width:1200px;text-align:center;font-size:12px;font-weight:500;letter-spacing:.3px;color:#444}
.to-top{position:absolute;left:1134px;top:310px;width:40px;height:40px;border-radius:50%;background:#dadada;display:flex;align-items:center;justify-content:center}
</style>
</head>
<body>
<div class="page">

  <!-- hero -->
  <svg class="hero-art" width="1200" height="830" viewBox="0 0 1200 830">
    <defs>
      <radialGradient id="heroTone" cx=".5" cy=".55" r=".6">
        <stop offset="0" stop-color="#8a8a8a"/>
        <stop offset=".6" stop-color="#4a4a4a"/>
        <stop offset="1" stop-color="#2b2b2b"/>
      </radialGradient>
    </defs>
    <rect width="1200" height="830" fill="url(#heroTone)" role="img" aria-label="Photo of a modern tower facade"/>
    <polygon points="0,767 1200,597 1200,830 0,830" fill="#ffffff"/>
    <polygon points="0,767 1200,597 0,812" fill="#dcdcdc"/>
  </svg>

  <div class="brand">Bright Vale</div>
  <ul class="nav">
    <li>HOME</li><li>ABOUT</li><li>TEAM</li><li>PORTFOLIO</li><li>NEWS</li><li>CONTACT US</li>
  </ul>
  <div class="slide-rail"><span></span></div>
  <div class="welcome">WELCOME TO</div>
  <h1 class="hero-title">Realestate</h1>
  <div class="btn-quote">REQUEST A QUOTE</div>
  <div class="scroll-btn">
    <svg width="26" height="30" viewBox="0 0 26 30"><path d="M13 2v25M3 17l10 10 10-10" fill="none" stroke="#222" stroke-width="2"/></svg>
  </div>

  <!-- about -->
  <div class="about-mark"></div>
  <h2 class="section-title" style="top:902px">About Us</h2>
  <p class="about-text">Proin gravida nibh vel velit auctor aliquet aenean sollicitudin lorem quis ipsum<br>nec sagittis sem nibh id elit. Duis sed odio sit amet nibh cursus sit amet mauris morbi<br>accumsan ipsum velit. Nam nec tellus a odio tincidunt auctor a ornare odio. Sed non<br>mauris vitae erat consequat auctor eu in elit aptent tacit...</p>
  <div class="text-link" style="left:538px;top:1124px">MORE ABOUT US...</div>

  <!-- feature slider -->
  <div class="feature">
    <h3>Real Estate</h3>
    <p>Proin gravida nibh vel velit auctor aliquet aenean sollicitudin lorem quis ipsum nec sagittis sem nibh id elit duis sed odio sit amet nibh</p>
  </div>
  <div class="photo" style="left:0;top:1451px;width:118px;height:362px;background:linear-gradient(160deg,#e8edf2,#8a6a55)" role="img" aria-label="Modern white house with timber panels"></div>
  <div class="photo" style="left:230px;top:1451px;width:674px;height:362px;background:linear-gradient(170deg,#cfd6dc 0%,#8c6a4e 45%,#6e7a5c 75%,#b9b9b4 100%);box-shadow:0 10px 30px rgba(0,0,0,.15)" role="img" aria-label="Contemporary office building with wide steps and garden"></div>
  <div class="photo" style="left:965px;top:1451px;width:235px;height:362px;background:linear-gradient(150deg,#a9cde6,#9a5a3e 70%,#6e3f2c)" role="img" aria-label="Brick high-rise against blue sky"></div>
  <div class="eye-btn">
    <svg width="22" height="14" viewBox="0 0 22 14"><path d="M1 7c3-5 7-6 10-6s7 1 10 6c-3 5-7 6-10 6S4 12 1 7z" fill="none" stroke="#222" stroke-width="1.6"/><circle cx="11" cy="7" r="2.6" fill="#222"/></svg>
  </div>
  <div class="text-link" style="left:230px;top:1862px">SEARCH 7,913 NO FEE APARTMENTS</div>
  <div class="pager">
    <svg width="16" height="10" viewBox="0 0 16 10"><path d="M15 5H2M6 1L2 5l4 4" fill="none" stroke="#888" stroke-width="1.4"/></svg>
    <span><b>2</b> / 3</span>
    <svg width="16" height="10" viewBox="0 0 16 10"><path d="M1 5h13M10 1l4 4-4 4" fill="none" stroke="#888" stroke-width="1.4"/></svg>
  </div>

  <!-- portfolio -->
  <svg class="portfolio-bg" width="1200" height="760" viewBox="0 0 1200 760">
    <defs>
      <linearGradient id="darkTone" x1="0" y1="0" x2="1" y2="1">
        <stop offset="0" stop-color="#3a3a3a"/><stop offset="1" stop-color="#242424"/>
      </linearGradient>
    </defs>
    <polygon points="0,0 1200,0 1200,702 0,529" fill="url(#darkTone)" role="img" aria-label="Darkened view of apartment balconies"/>
    <polygon points="0,529 1200,702 1200,751" fill="#dcdcdc"/>
  </svg>
  <h2 class="section-title on-dark" style="top:2172px">Our Portfolio</h2>
  <div class="photo" style="left:89px;top:2268px;width:246px;height:312px;background:linear-gradient(180deg,#a8c8e0 0%,#e9e4df 45%,#3fa7c4 80%,#6e8a4c 100%)" role="img" aria-label="Villa with swimming pool"></div>
  <div class="photo" style="left:346px;top:2268px;width:248px;height:312px;background:linear-gradient(180deg,#bcd4e6 0%,#9a6a48 45%,#b45a3c 100%)" role="img" aria-label="Timber and brick townhouse"></div>
  <div class="photo" style="left:604px;top:2268px;width:248px;height:312px;background:linear-gradient(180deg,#dfe3e6 0%,#f3f3f1 50%,#8aa070 100%)" role="img" aria-label="White cubic house with lawn"></div>
  <div class="photo" style="left:863px;top:2268px;width:246px;height:312px;background:linear-gradient(160deg,#cfe0ec 0%,#f1efea 50%,#c9b8a6 100%)" role="img" aria-label="White apartment block with balconies"></div>

  <!-- testimonials -->
  <h2 class="section-title" style="top:2826px">Testimonials</h2>
  <div class="testimonial" style="left:93px;top:2974px">
    <div class="quote-mark">“</div>
    <div class="avatar" role="img" aria-label="Client portrait"></div>
    <blockquote>Duis sed odio sit amet nibh vulputate cursus a sit amet mauris. Morbi accumsan ipsum velit. Nam nec tellus a odio tincidunt auctor...</blockquote>
    <div class="who">-DANIEL K. MERCER</div>
    <div class="role">Manager</div>
  </div>
  <div class="testimonial" style="left:630px;top:2974px">
    <div class="quote-mark">“</div>
    <div class="avatar" role="img" aria-label="Client portrait"></div>
    <blockquote>Duis sed odio sit amet nibh vulputate cursus a sit amet mauris. Morbi accumsan ipsum velit. Nam nec tellus a odio tincidunt auctor...</blockquote>
    <div class="who">-DANIEL K. MERCER</div>
    <div class="role">Manager</div>
  </div>
  <div class="divider" style="top:3211px"></div>

  <!-- news -->
  <h2 class="section-title" style="top:3285px">Latest News</h2>
  <article class="news-card" style="left:89px">
    <div class="photo" style="background:linear-gradient(150deg,#9a9a9a,#dcdcdc 40%,#3c6a8a 70%,#c9d3da)" role="img" aria-label="Glass and concrete building facade"></div>
    <span class="tag">NEWS</span>
    <h4>Some news heading goes here...</h4>
    <div class="date"><svg width="12" height="12" viewBox="0 0 12 12"><rect x="1" y="2" width="10" height="9" fill="none" stroke="#aaa"/><path d="M1 5h10" stroke="#aaa"/></svg>25-08-2018</div>
    <p>Aenean vulputate eleifend tellus aenean leo ligula, porttitor eu conse quat vitae eleifend ac enim..</p>
  </article>
  <article class="news-card" style="left:617px">
    <div class="photo" style="background:linear-gradient(160deg,#6a7a80,#c9cfcf 50%,#8d9396)" role="img" aria-label="Hands working at a laptop with paperwork"></div>
    <span class="tag">NEWS</span>
    <h4>Some news heading goes here...</h4>
    <div class="date"><svg width="12" height="12" viewBox="0 0 12 12"><rect x="1" y="2" width="10" height="9" fill="none" stroke="#aaa"/><path d="M1 5h10" stroke="#aaa"/></svg>25-08-2018</div>
    <p>Aenean vulputate eleifend tellus aenean leo ligula, porttitor eu conse quat vitae eleifend ac enim..</p>
  </article>

  <!-- newsletter -->
  <section class="newsletter">
    <div class="kicker">Subscribe</div>
    <h5>Newsletter</h5>
    <div class="note">By subscribing to our mailing list you will always be updated...</div>
    <div class="signup">
      <div class="field"><svg width="16" height="12" viewBox="0 0 16 12"><rect x=".5" y=".5" width="15" height="11" fill="none" stroke="#aaa"/><path d="M1 1l7 6 7-6" fill="none" stroke="#aaa"/></svg>Enter your email address</div>
      <div class="go">SUBSCRIBE</div>
    </div>
  </section>

  <!-- footer -->
  <footer class="footer">
    <div class="brand-big">Bright Vale</div>
    <div class="brand-sub">GROUP</div>
    <div class="col" style="left:449px">
      <h6>Quick Links</h6>
      <ul><li>Home</li><li>About Us</li><li>Our Team</li><li>Portfolio</li><li>News</li><li>Contact Us</li></ul>
    </div>
    <div class="col" style="left:658px">
      <h6>Information</h6>
      <ul><li>Site Map</li><li>Terms &amp; Condition</li><li>Privacy Policy</li><li>FAQ's</li><li>Customer Service</li><li>Disclaimer</li></ul>
    </div>
    <div class="col contact" style="left:865px">
      <h6>Contact Us</h6>
      <ul>
        <li><svg width="14" height="12" viewBox="0 0 14 12"><rect width="14" height="11" fill="#222"/><path d="M0 0l7 6 7-6" fill="none" stroke="#fff"/></svg><span>Email:<br>info@bright-vale.net</span></li>
        <li><svg width="14" height="14" viewBox="0 0 14 14"><path d="M3 1l3 3-2 2c1 2 2 3 4 4l2-2 3 3-2 2C6 13 1 8 1 3z" fill="#222"/></svg><span>Phone:<br>(+08) 123 456 7890</span></li>
        <li><svg width="12" height="16" viewBox="0 0 12 16"><path d="M6 0a6 6 0 0 1 6 6c0 4-6 10-6 10S0 10 0 6a6 6 0 0 1 6-6z" fill="#222"/><circle cx="6" cy="6" r="2" fill="#fff"/></svg><span>Office Location:<br>Some address line goes here<br>city name</span></li>
      </ul>
    </div>
    <div class="rule"></div>
    <div class="to-top"><svg width="12" height="14" viewBox="0 0 12 14"><path d="M6 13V2M2 6l4-4 4 4" fill="none" stroke="#444" stroke-width="1.4"/></svg></div>
    <div class="copy">© COPYRIGHT 2021 BRIGHT VALE GROUP – ALL RIGHTS RESERVED</div>
  </footer>

</div>
</body>
</html>
```